Unique business card design

Boutique coastal hotel suites - in need of clever stand out business card I have uploaded the logo that I had created through quill forge I want something that is clever and stands out from everyone else - 418 Brantwell Avenue seldovia Alaska 99571 phone or text 907 -581-6142 www.primemarrowbysuites.com

Target Market(s)

Men and woman

Industry/Entity Type

Boutique coastal hotel

Contact Information for Business Card

Marrowby Suites Seldovia Alaska marrowby_suites@mailnest.net

Requirements
Must have
• Classy - clever -bold 907-581-6142 call or text

```html
<!DOCTYPE html>
<html lang="en">
<head>
<meta charset="UTF-8">
<title>Marrowby Suites – Business Card</title>
<link href="https://fonts.googleapis.com/css2?family=Poppins:wght@400;500;600;700&display=swap" rel="stylesheet">
<style>
  :root {
    --paper: #efebe5;
    --navy: #2c5272;
    --red: #d22127;
    --ink: #111111;
    --gold: #f2c733;
    --white: #ffffff;
    --backdrop: #d9d9d9;
  }
  * { box-sizing: border-box; margin: 0; padding: 0; }
  html, body {
    width: 1200px; height: 900px; overflow: hidden;
    background: var(--backdrop);
    font-family: "Poppins", sans-serif;
  }
  .canvas { position: relative; width: 1200px; height: 900px; }

  .card {
    position: absolute;
    width: 600px; height: 340px;
    background: var(--paper);
    border-radius: 22px;
    overflow: hidden;
    box-shadow: 0 10px 24px rgba(0,0,0,0.25);
  }
  .card--front { left: 80px; top: 80px; }
  .card--back { left: 520px; top: 480px; }

  .wordmark {
    display: flex; align-items: center; gap: 12px;
    color: var(--navy);
    font-weight: 600;
    letter-spacing: 0.04em;
  }
  .wordmark__mark { width: 20px; height: 20px; background: var(--navy); flex: none; }

  .card--front .wordmark {
    position: absolute; left: 0; right: 0; top: 112px;
    justify-content: center; font-size: 40px;
  }
  .front-band {
    position: absolute; left: 0; right: 0; bottom: 0; height: 68px;
    background: var(--navy);
    display: flex; align-items: center; justify-content: center;
    color: var(--white); font-size: 15px; letter-spacing: 0.02em;
  }

  .card--back .wordmark {
    position: absolute; left: 40px; top: 96px; font-size: 30px;
  }
  .logo-rule {
    position: absolute; left: 40px; top: 152px; width: 290px; height: 2px;
    background: var(--ink);
  }
  .phone-block {
    position: absolute; right: 30px; top: 30px;
    display: flex; align-items: center; gap: 14px;
  }
  .phone-block__text { text-align: right; line-height: 1.1; }
  .phone-block__label { color: var(--red); font-size: 12px; font-weight: 600; text-transform: uppercase; }
  .phone-block__number { color: var(--ink); font-size: 26px; font-weight: 700; }
  .phone-block__icon { width: 38px; height: 38px; flex: none; }

  .sweep { position: absolute; inset: 0; width: 600px; height: 340px; }

  .contact-list {
    position: absolute; right: 30px; bottom: 30px;
    list-style: none; text-align: right;
    color: var(--white); font-size: 14px; line-height: 1.8;
  }
  .contact-list li { display: flex; align-items: center; justify-content: flex-end; gap: 10px; }
  .contact-list svg { width: 16px; height: 16px; flex: none; }
</style>
</head>
<body>
<main class="canvas">

  <section class="card card--front" aria-label="Card front">
    <div class="wordmark"><span class="wordmark__mark"></span>Marrowby Suites</div>
    <div class="front-band">www.primemarrowbysuites.com</div>
  </section>

  <section class="card card--back" aria-label="Card back">
    <svg class="sweep" viewBox="0 0 600 340" aria-hidden="true">
      <polygon points="0,268 572,112 0,296" fill="var(--red)"/>
      <polygon points="0,316 600,104 600,340 0,340" fill="var(--navy)"/>
    </svg>

    <div class="wordmark"><span class="wordmark__mark"></span>Marrowby Suites</div>
    <div class="logo-rule"></div>

    <div class="phone-block">
      <div class="phone-block__text">
        <div class="phone-block__label">Call or text</div>
        <div class="phone-block__number">907 -581-6142</div>
      </div>
      <svg class="phone-block__icon" viewBox="0 0 38 38" aria-hidden="true">
        <circle cx="19" cy="19" r="19" fill="var(--red)"/>
        <path d="M13 12c1-1 2-1 3 0l2 3c.5 1 0 2-1 2.5-.5.3-.5 1 0 2l1.5 1.5c1 .5 1.7.5 2 0 .5-1 1.5-1.5 2.5-1l3 2c1 1 1 2 0 3-2 2-5 2-9-2s-5-8-4-11z" fill="var(--white)"/>
      </svg>
    </div>

    <ul class="contact-list">
      <li>marrowby_suites@mailnest.net
        <svg viewBox="0 0 16 16" aria-hidden="true"><rect x="1" y="3" width="14" height="10" fill="var(--gold)"/><path d="M1 3l7 6 7-6" fill="none" stroke="var(--navy)" stroke-width="1.2"/></svg>
      </li>
      <li>www.primemarrowbysuites.com
        <svg viewBox="0 0 16 16" aria-hidden="true"><g fill="none" stroke="var(--gold)" stroke-width="1.3"><circle cx="8" cy="8" r="6.5"/><ellipse cx="8" cy="8" rx="3" ry="6.5"/><path d="M1.5 8h13M3 4.5h10M3 11.5h10"/></g></svg>
      </li>
      <li>418 Brantwell Avenue kelvaro, Alaska 99571
        <svg viewBox="0 0 16 16" aria-hidden="true"><path d="M8 15s5-5 5-9a5 5 0 0 0-10 0c0 4 5 9 5 9z" fill="var(--gold)"/><circle cx="8" cy="6" r="2" fill="var(--navy)"/></svg>
      </li>
    </ul>
  </section>

</main>
</body>
</html>
```